Kelvar Systems Website

Website design for our company: Kelvar Systems.
The website should look fresh and IT focused. Please have a look at http://www.kelvarsystems.net.au/ for our current design. We want something fresh and new, professional looking, in WordPress so we can easily make changes.

Industry/Entity Type

It Company

```html
<!DOCTYPE html>
<html lang="en">
<head>
<meta charset="utf-8">
<title>Kelvar Systems</title>
<link rel="stylesheet" href="https://fonts.googleapis.com/css2?family=PT+Sans:wght@400;700&family=Arimo:wght@400;700&display=swap">
<style>
:root{
  --ink-dark:#27363d;
  --green:#0fbf62;
  --green-deep:#0a9e50;
  --green-text:#12a45a;
  --hero-light:#e4e4e4;
  --hero-mid:#d5d5d5;
  --band-grey:#e6e6e6;
  --page-bg:#f3f2ee;
  --white:#ffffff;
  --text:#555555;
  --footer:#444444;
  --footer-base:#363636;
  --footer-text:#bbbbbb;
  --line:#dddddd;
}
*{box-sizing:border-box;margin:0;padding:0}
html,body{width:1200px;height:1134px;overflow:hidden}
body{position:relative;background:var(--page-bg);font-family:"Arimo",Arial,sans-serif;color:var(--text)}
.abs{position:absolute}
.heading{font-family:"PT Sans",Arial,sans-serif}

.topbar{left:0;top:0;width:1200px;height:34px;background:var(--ink-dark)}
.brand{left:327px;top:10px;width:85px;height:43px;background:var(--white);border:2px solid var(--green);border-radius:3px;display:flex;align-items:center;justify-content:center;gap:5px;z-index:2}
.brand-dot{width:9px;height:9px;border-radius:50%;background:var(--green)}
.brand-name{font-family:"PT Sans",Arial,sans-serif;font-weight:700;font-size:10px;color:var(--green-deep)}
.nav{right:288px;top:0;height:34px;display:flex;gap:13px;align-items:center}
.nav a{font-family:"PT Sans",Arial,sans-serif;font-size:9px;font-weight:700;color:var(--white);text-decoration:none;letter-spacing:.3px}
.nav a.current{color:var(--green)}

.hero{left:0;top:34px;width:1200px;height:295px;background:linear-gradient(160deg,var(--hero-light) 0%,var(--hero-mid) 55%,var(--hero-light) 100%)}
.hero-kicker{left:327px;top:139px;font-size:14px;color:var(--green-text)}
.hero-title{left:327px;top:155px;font-size:19px;font-weight:700;color:var(--green-text);letter-spacing:.5px}
.hero-copy{left:327px;top:190px;width:180px;font-size:9.5px;line-height:11.5px;color:#666}
.btn-green{background:var(--green);color:var(--white);font-family:"PT Sans",Arial,sans-serif;font-weight:700;display:flex;align-items:center;justify-content:center;border-radius:2px;box-shadow:0 2px 2px rgba(0,0,0,.2)}
.hero-btn{left:327px;top:240px;width:88px;height:30px;font-size:10.5px;letter-spacing:.5px}
.hero-art{left:528px;top:118px;width:385px;height:172px;border-radius:10px;background:radial-gradient(ellipse at center,#7d8a93 0%,#b8c0c4 45%,rgba(220,220,220,0) 75%)}

.strip{left:0;top:329px;width:1200px;height:37px;background:var(--ink-dark)}
.strip-text{left:327px;top:344px;font-family:"PT Sans",Arial,sans-serif;font-size:8px;color:var(--white);white-space:nowrap}
.strip-btn{left:821px;top:333px;width:91px;height:29px;font-size:12px}

.remote{left:0;top:366px;width:1200px;height:76px;background:var(--band-grey);border-bottom:1px solid #d2d2d2}
.remote-label{left:327px;top:398px;font-size:12px;color:#666;letter-spacing:.5px}
.field{background:var(--white);border:1px solid #c9c9c9;font-size:9px;color:#999;display:flex;align-items:center;padding-left:10px}
.code-field{left:454px;top:391px;width:177px;height:27px}
.connect-btn{left:634px;top:391px;width:91px;height:27px;font-size:9px;font-family:"Arimo",Arial,sans-serif}
.search-field{left:735px;top:391px;width:177px;height:27px;border-color:#fff;padding-left:14px}

.panel{background:var(--white);border:1px solid #e4e4e4}
.profile{left:327px;top:474px;width:398px;height:237px}
.tabs{left:327px;top:474px;width:398px;height:33px;display:flex}
.tab{font-size:10px;display:flex;align-items:center;padding:0 16px;color:var(--white);background:linear-gradient(var(--green),var(--green-deep))}
.tab.active{background:var(--white);color:#666;width:107px;justify-content:center}
.tab.fill{flex:1}
.tab-divider{border-left:1px solid #0b9b4f}
.profile-art{left:338px;top:544px;width:87px;height:97px;background:linear-gradient(160deg,#3b78c8,#c9d6e2 60%,#eeeeee);border-radius:6px}
.profile-copy{left:436px;top:533px;width:278px;font-size:8.3px;line-height:10.3px;color:#666}
.profile-copy p{margin-bottom:9px}

.testimonial{left:327px;top:727px;width:398px;height:160px}
.testi-title{left:345px;top:746px;font-size:11px;color:#666;letter-spacing:.3px}
.testi-photo{left:345px;top:777px;width:90px;height:60px;background:linear-gradient(135deg,#6b4a3a,#d9a98e 55%,#f0d8c8)}
.quote-mark{font-family:"PT Sans",Arial,sans-serif;font-size:28px;font-weight:700;color:var(--green);line-height:1}
.q-open{left:446px;top:772px}
.q-close{left:692px;top:818px}
.testi-copy{left:448px;top:792px;width:250px;font-size:8.3px;line-height:10.5px;color:#666}
.testi-rule{left:345px;top:845px;width:361px;height:1px;background:var(--line)}
.testi-name{right:494px;top:851px;font-size:11px;color:var(--green-text)}
.testi-role{right:494px;top:867px;font-size:7.5px;color:#666}

.card{left:736px;width:176px;height:121px}
.card-onsite{top:474px}
.card-remote{top:604px}
.card-art{left:7px;top:8px;width:64px;height:68px;border-radius:4px}
.card-onsite .card-art{background:linear-gradient(150deg,#5fa35a,#c9d8e4 55%,#f4f4f4)}
.card-remote .card-art{background:radial-gradient(circle at 45% 50%,#7a7a7a,#c8c8c8 55%,#f2f2f2)}
.card-title{left:77px;top:9px;font-size:8.5px;color:var(--green-text);white-space:nowrap}
.card-copy{left:77px;top:31px;width:92px;font-size:6.8px;line-height:10.5px;color:#777}
.see-more{left:89px;top:87px;width:73px;height:23px;background:linear-gradient(#eeeeee,#c5c5c5);border:1px solid #b5b5b5;border-radius:2px;font-size:7px;color:#888;display:flex;align-items:center;padding-left:11px}
.see-more svg{position:absolute;right:6px;top:4px}
.services-btn{left:736px;top:744px;width:176px;height:35px;font-size:11px;font-family:"Arimo",Arial,sans-serif;border:1px solid var(--green-deep)}

.footer{left:0;top:913px;width:1200px;height:189px;background:var(--footer)}
.foot-title{font-size:12px;color:#e4e4e4;letter-spacing:.5px;top:938px}
.contact-list{left:327px;top:966px;font-size:8.5px;color:var(--footer-text);line-height:14px}
.contact-row{display:flex;gap:10px;margin-bottom:3px}
.contact-row svg{flex:none;margin-top:2px}
.tweet{left:502px;width:205px;font-size:8px;line-height:11px;color:#999}
.tweet b{font-weight:400;color:var(--green)}
.tweet small{display:block;font-size:6.5px;color:#ddd;margin-top:3px}
.tweet-rule{left:502px;top:1008px;width:205px;height:1px;background:#555}
.email-field{left:752px;top:968px;width:160px;height:31px;border:1px solid #777;background:#3c3c3c;font-size:8px;color:#999;display:flex;align-items:center;padding-left:10px}
.email-field svg{position:absolute;right:14px;top:10px}
.socials{left:753px;top:1045px;display:flex;gap:5px}
.socials span{width:17px;height:17px;border-radius:50%;background:#cfcfcf}
.base{left:0;top:1102px;width:1200px;height:32px;background:var(--footer-base)}
.copyright{left:327px;top:1118px;font-size:6.5px;color:#cccccc}
.foot-nav{right:288px;top:1116px;display:flex;gap:12px}
.foot-nav a{font-family:"PT Sans",Arial,sans-serif;font-size:7.5px;color:#dddddd;text-decoration:none;letter-spacing:.3px}
</style>
</head>
<body>

<header>
  <div class="abs topbar"></div>
  <div class="abs brand"><span class="brand-dot"></span><span class="brand-name">Kelvar Systems</span></div>
  <nav class="abs nav">
    <a class="current" href="#">HOME</a><a href="#">CLIENTS</a><a href="#">SERVICES</a><a href="#">SUPPORTS</a><a href="#">TESTIMONIALS</a><a href="#">CONTACT US</a><a href="#">ABOUT US</a>
  </nav>
</header>

<section class="hero-section">
  <div class="abs hero" role="img" aria-label="Brushed metal texture background"></div>
  <div class="abs hero-kicker heading">Simplify</div>
  <div class="abs hero-title heading">YOUR BUSINESS</div>
  <div class="abs hero-copy heading">Create a refreshing customer experience that's free of complexity and confusion</div>
  <div class="abs btn-green hero-btn">READ MORE</div>
  <div class="abs hero-art" role="img" aria-label="Laptop showing the website, surrounded by colourful puzzle pieces and a dotted world map"></div>
</section>

<section>
  <div class="abs strip"></div>
  <div class="abs strip-text">Kelvar Systems is an Adelaide based company with a single objective - to excel in the support and service of all computer and IT needs</div>
  <div class="abs btn-green strip-btn">Contact Us !</div>
</section>

<section>
  <div class="abs remote"></div>
  <div class="abs remote-label heading">REMOTE SERVICE</div>
  <div class="abs field code-field">Enter your 6-digit code</div>
  <div class="abs btn-green connect-btn">CONNECT NOW !</div>
  <div class="abs field search-field">Search Keyword</div>
</section>

<main>
  <div class="abs panel profile"></div>
  <div class="abs tabs">
    <div class="tab active">Company Profile</div>
    <div class="tab">Services</div>
    <div class="tab fill tab-divider">Remote Login</div>
  </div>
  <div class="abs profile-art" role="img" aria-label="Computer monitor with a blue globe"></div>
  <div class="abs profile-copy">
    <p>Kelvar Systems is an Adelaide based company with a single objective - to excel in the support and service of all computer and IT needs.</p>
    <p>We provide a high level of consulting services using the most experienced engineers at a reasonable and fair price. We believe in using a Business Value approach to every aspect of computer consulting to provide our clients with the most cost effective solutions.</p>
    <p>We strongly believe that we are in business with our clients. Each thing we do must be measured against our clients' business objectives. At the end of the day our client's success is our success.</p>
  </div>

  <div class="abs panel testimonial"></div>
  <div class="abs testi-title">CLIENTS TESTIMONIAL</div>
  <div class="abs testi-photo" role="img" aria-label="Portrait photo of a client"></div>
  <div class="abs quote-mark q-open">&ldquo;</div>
  <div class="abs testi-copy">Lorem Ipsum is simply dummy text of the printing and typesetting industry. Lorem Ipsum has been the industry's standard dummy text ever since the 1500s</div>
  <div class="abs quote-mark q-close">&rdquo;</div>
  <div class="abs testi-rule"></div>
  <div class="abs testi-name">Norvane Technology</div>
  <div class="abs testi-role">Web Design &amp; Developer, IND</div>

  <div class="abs panel card card-onsite">
    <div class="abs card-art" role="img" aria-label="Growth bar chart over documents"></div>
    <div class="abs card-title">On-site Service</div>
    <div class="abs card-copy">Lorem Ipsum is simply dummy text of the printing and typeset-ting industry. Lorem Ipsum has been.</div>
    <div class="abs see-more">See More<svg width="14" height="14" viewBox="0 0 14 14"><circle cx="7" cy="7" r="6.5" fill="#9a9a9a"/><path d="M6 4l3 3-3 3" stroke="#fff" stroke-width="1.5" fill="none"/></svg></div>
  </div>
  <div class="abs panel card card-remote">
    <div class="abs card-art" role="img" aria-label="Silver compass clock"></div>
    <div class="abs card-title">Remote Desktop Support</div>
    <div class="abs card-copy">Lorem Ipsum is simply dummy text of the printing and typeset-ting industry. Lorem Ipsum has been.</div>
    <div class="abs see-more">See More<svg width="14" height="14" viewBox="0 0 14 14"><circle cx="7" cy="7" r="6.5" fill="#9a9a9a"/><path d="M6 4l3 3-3 3" stroke="#fff" stroke-width="1.5" fill="none"/></svg></div>
  </div>
  <div class="abs btn-green services-btn">See List Of Our Services</div>
</main>

<footer>
  <div class="abs footer"></div>
  <div class="abs foot-title heading" style="left:327px">CONTACT US</div>
  <div class="abs contact-list">
    <div class="contact-row"><svg width="12" height="11" viewBox="0 0 12 11"><path d="M1 5L6 1l5 4v5H1z" fill="none" stroke="#bbb"/></svg><span>118 Harbour Lane<br>Ridgefield<br>5098<br>Australia</span></div>
    <div class="contact-row" style="margin-top:6px"><svg width="12" height="10" viewBox="0 0 12 10"><path d="M2 1l2 0 1 2-1 1c1 2 2 3 4 4l1-1 2 1v2c-5 0-9-4-9-9z" fill="#bbb"/></svg><span>0870001111</span></div>
    <div class="contact-row"><svg width="12" height="10" viewBox="0 0 12 10"><rect x="2" y="1" width="7" height="8" fill="#bbb"/></svg><span>087000 2200</span></div>
    <div class="contact-row"><svg width="12" height="10" viewBox="0 0 12 10"><rect x="3" y="0" width="5" height="10" rx="1" fill="none" stroke="#bbb"/></svg><span>0870001111</span></div>
  </div>

  <div class="abs foot-title heading" style="left:502px">GET IN TWEET</div>
  <div class="abs tweet" style="top:967px"><b>@companyname</b> Lorem Ipsum is simply dummy text of the printing and typesetting industry<small>5 min ago</small></div>
  <div class="abs tweet-rule"></div>
  <div class="abs tweet" style="top:1020px"><b>@companyname</b> Lorem Ipsum is simply dummy text of the printing and typesetting industry<small>5 min ago</small></div>

  <div class="abs foot-title heading" style="left:753px">NEWSLETTER SIGNUP</div>
  <div class="abs email-field">Your Email<svg width="6" height="10" viewBox="0 0 6 10"><path d="M1 1l4 4-4 4" stroke="#0fbf62" stroke-width="1.5" fill="none"/></svg></div>
  <div class="abs foot-title heading" style="left:753px;top:1021px">FOLLOW US</div>
  <div class="abs socials" aria-label="Social profiles"><span></span><span></span><span></span><span></span><span></span><span></span></div>

  <div class="abs base"></div>
  <div class="abs copyright">Copyright &copy; 2014 Kelvar Systems Pty Ltd. All Rights Reserved.</div>
  <nav class="abs foot-nav">
    <a href="#">HOME</a><a href="#">CLIENTS</a><a href="#">SERVICES</a><a href="#">SUPPORTS</a><a href="#">TESTIMONIALS</a><a href="#">CONTACT US</a><a href="#">ABOUT US</a>
  </nav>
</footer>

</body>
</html>
```